Mobile Tutoring Service needs a Flier for Distribution to Clients

Lantern Scholars Inc. is a tutoring company that uses video call technology to perform tutoring session in math, sciences, and standardized test preparation. We need a flier that we can distribute to email lists of parents in school districts around the St. Louis Area, as well as post in public areas to attract clients. The following file has the important information needed on the flier. In particular, the "How it Works" Steps 1-3 can be made into an animation or video that looks attractive and helps potential clients understand our process. Our logo is also found in the document. Ideally, all information in the power point slide will be in the flier.

Target Market(s)

Parents for middle and high schoolers grade 6-12 in the St. Louis Area

Industry/Entity Type

Tutoring

Font styles to use
Serif

Colors
3176b5
85abd2
0492cd
33a6d7
ceeaf5

Requirements
Must have
• All the information with the attached file
Nice to have
• A nice-looking animation instead of the still screen shoots that are included in the attached file.

```html
<!DOCTYPE html>
<html lang="en">
<head>
<meta charset="utf-8">
<title>Lantern Scholars Flier</title>
<link rel="stylesheet" href="https://fonts.googleapis.com/css2?family=Roboto+Condensed:wght@400;700&display=swap">
<style>
  :root{
    --page-bg:#1d5f8f;
    --header-blue:#5591d0;
    --accent-blue:#4f90d6;
    --ink:#1f1f1f;
    --white:#ffffff;
    --footer-gray:#5c5c5c;
    --thumb-fill:#d9d5cf;
  }
  *{margin:0;padding:0;box-sizing:border-box}
  html,body{width:1200px;height:1200px;overflow:hidden}
  body{background:var(--page-bg);font-family:"Roboto Condensed","Arial Narrow",sans-serif;position:relative}
  .flier{
    position:absolute;left:146px;top:20px;width:991px;height:1268px;
    transform:scale(0.915);transform-origin:0 0;overflow:hidden;
    box-shadow:0 14px 30px rgba(0,0,0,.45);
  }
  .flier-bg{position:absolute;inset:0}
  .abs{position:absolute}
  .brand{left:40px;top:60px;width:270px;text-align:center}
  .brand-mark{width:110px;height:110px;border-radius:50%;background:var(--white);margin:0 auto 38px}
  .brand-name{font-weight:700;font-size:36px;color:var(--ink);line-height:1}
  .headline{left:360px;top:46px;color:var(--white);font-weight:700;line-height:1.1}
  .headline .lead{font-size:53px;display:block}
  .headline .big{font-size:91px;display:block;line-height:.98;margin-top:6px}
  .step-thumb{left:56px;width:170px;height:160px}
  .step-arrow{left:238px;width:20px;height:46px}
  .step-text{left:270px;color:var(--white)}
  .step-text h3{font-size:28px;font-weight:700;line-height:1.1}
  .step-text p{font-size:19px;line-height:1.2}
  .hand-phone{left:245px;top:872px;width:180px;height:133px;border-radius:34px 34px 0 0;
    background:linear-gradient(160deg,#d7b9a4 0%,#b89582 45%,#2c2c2c 100%)}
  .info{left:534px;width:430px;color:var(--white)}
  .info h2{color:var(--accent-blue);font-weight:700;font-size:28px;line-height:1.05}
  .info p{font-size:23px;line-height:1.22}
  .info p b{font-weight:700}
  .plans-banner{left:520px;top:663px;width:335px;height:52px}
  .plans-title{left:533px;top:663px;font-size:37px;font-weight:700;color:var(--white);line-height:52px}
  .price{left:534px;top:866px;width:490px;height:96px}
  .price-amount{left:534px;top:890px;width:96px;text-align:center;color:var(--white);font-weight:700;font-size:33px}
  .price-term{left:642px;top:894px;color:var(--white);font-size:26px}
  .contact{left:0;width:991px;text-align:center;color:var(--white)}
  .contact-head{top:1028px;font-weight:700;font-size:41px;line-height:1.05}
  .contact-sub{top:1072px;font-weight:700;font-size:34px}
  .contact-rule{left:100px;top:1127px;width:795px;height:1px;background:#9a9a9a}
  .contact-phone{top:1140px;font-weight:700;font-size:46px}
  .contact-web{top:1192px;font-size:25px}
</style>
</head>
<body>
<main class="flier">
  <svg class="flier-bg" viewBox="0 0 991 1268" width="991" height="1268" aria-hidden="true">
    <defs>
      <radialGradient id="darkGlow" cx="0.35" cy="0.45" r="0.7">
        <stop offset="0" stop-color="#5a5454"/>
        <stop offset="0.6" stop-color="#1c1a1a"/>
        <stop offset="1" stop-color="#000"/>
      </radialGradient>
    </defs>
    <rect width="991" height="1268" fill="#000"/>
    <polygon points="0,390 320,278 991,278 991,888 672,1005 0,1005" fill="url(#darkGlow)"/>
    <polygon points="0,0 991,0 991,273 318,273 0,384" fill="var(--header-blue)"/>
    <polyline points="0,390 320,278 991,278" fill="none" stroke="#fff" stroke-width="6"/>
    <polygon points="0,1008 672,1008 991,892 991,1268 0,1268" fill="var(--footer-gray)"/>
    <polyline points="0,1005 672,1005 991,889" fill="none" stroke="#fff" stroke-width="6"/>
  </svg>

  <div class="abs brand">
    <div class="brand-mark"></div>
    <div class="brand-name">Lantern Scholars</div>
  </div>

  <h1 class="abs headline">
    <span class="lead">Personalized Tutoring From</span>
    <span class="lead">STEM Experts Via Your</span>
    <span class="big">MOBILE DEVICE</span>
  </h1>

  <!-- How it works -->
  <svg class="abs step-thumb" style="top:398px" viewBox="0 0 170 160">
    <polygon points="2,2 168,2 168,105 85,155 2,105" fill="#fff" stroke="var(--accent-blue)" stroke-width="3"/>
    <rect x="24" y="16" width="120" height="90" fill="var(--thumb-fill)" role="img" aria-label="Photo of a handwritten math problem"/>
  </svg>
  <svg class="abs step-arrow" style="top:428px" viewBox="0 0 20 46"><polygon points="2,0 18,23 2,46 8,23" fill="#fff"/></svg>
  <div class="abs step-text" style="top:422px"><h3>STEP 1</h3><p>Send tutors your problem</p></div>

  <svg class="abs step-thumb" style="top:573px" viewBox="0 0 170 160">
    <polygon points="2,2 168,2 168,105 85,155 2,105" fill="#e8f4fc" stroke="var(--accent-blue)" stroke-width="3"/>
    <rect x="6" y="6" width="158" height="100" fill="#e2f0fa" role="img" aria-label="Screenshot of a chat message from a tutor"/>
  </svg>
  <svg class="abs step-arrow" style="top:603px" viewBox="0 0 20 46"><polygon points="2,0 18,23 2,46 8,23" fill="#fff"/></svg>
  <div class="abs step-text" style="top:586px"><h3>STEP 2</h3><p>Tutor sends response to set<br>Up session</p></div>

  <svg class="abs step-thumb" style="top:748px" viewBox="0 0 170 160">
    <polygon points="2,2 168,2 168,105 85,155 2,105" fill="#e8f4fc" stroke="var(--accent-blue)" stroke-width="3"/>
    <rect x="24" y="14" width="124" height="100" fill="#cfc9c6" role="img" aria-label="Photo of whiteboard notes from a session"/>
  </svg>
  <svg class="abs step-arrow" style="top:778px" viewBox="0 0 20 46"><polygon points="2,0 18,23 2,46 8,23" fill="#fff"/></svg>
  <div class="abs step-text" style="top:762px"><h3>STEP 3</h3><p>Perform tutoring session and<br>Receive copy of your notes!</p></div>

  <div class="abs hand-phone" role="img" aria-label="Hand holding a smartphone showing the app"></div>

  <!-- Service details -->
  <section class="abs info" style="top:305px">
    <h2>SUBJECTS</h2>
    <p>All Math, Science, Standardized Test Prep,<br>and Writing 6th-12th grade.</p>
  </section>
  <section class="abs info" style="top:411px">
    <h2>OUR TUTORS ARE LOCAL</h2>
    <p>St. Louis PhD candidates or<br>PhD degree holders in STEM fields.</p>
  </section>
  <section class="abs info" style="top:518px">
    <h2>NO SCHEDULING REQUIRED!</h2>
    <p>As soon as you send a message for help,<br>a tutor will respond to set up a study session<br>as soon as possible.</p>
  </section>

  <svg class="abs plans-banner" viewBox="0 0 335 52" aria-hidden="true">
    <polygon points="0,0 290,0 330,52 0,52" fill="#fff"/>
    <polygon points="0,0 283,0 320,52 0,52" fill="var(--accent-blue)"/>
  </svg>
  <div class="abs plans-title">PAYMENT PLANS</div>

  <section class="abs info" style="top:725px">
    <h2>PAY-AS-YOU-GO</h2>
    <p><b>$0.83</b>/ minute. <b>$0</b> up-front<br>before session begins!</p>
  </section>
  <section class="abs info" style="top:831px">
    <h2>UNLIMITED SUBSCRIPTION</h2>
  </section>

  <svg class="abs price" viewBox="0 0 490 96" aria-hidden="true">
    <polygon points="60,16 210,16 230,48 210,80 60,80" fill="var(--accent-blue)"/>
    <polyline points="70,22 206,22 222,48 206,74 70,74" fill="none" stroke="#fff" stroke-width="1.2" stroke-dasharray="4 3"/>
    <circle cx="48" cy="48" r="46" fill="var(--accent-blue)" stroke="#2c5f98" stroke-width="2"/>
    <circle cx="48" cy="48" r="40" fill="none" stroke="#fff" stroke-width="1.2" stroke-dasharray="4 3"/>
  </svg>
  <div class="abs price-amount">$150</div>
  <div class="abs price-term">Per Month</div>

  <!-- Contact -->
  <div class="abs contact contact-head">CONTACT US TODAY</div>
  <div class="abs contact contact-sub">TO SET UP FOR YOUR FIRST, FREE TUTORING SESSION</div>
  <div class="abs contact-rule"></div>
  <div class="abs contact contact-phone">Phone : 866-555-0142</div>
  <div class="abs contact contact-web">www.lanternscholars.com &nbsp;|&nbsp; tutor@lanternscholars.com</div>
</main>
</body>
</html>
```